Interior Design/ decoration business card design

This card is for my Interior Design and Decoration business and later I will also be selling homewares. I would like the card to be very simple in design and like either white, duck egg blue , aquas or metallics on a flat mat card excellent quality card. It needs to be well designed as that is my field. I dont like fuss, the simpler the better. I would like a styalised wren under the name wren if possible. SIMPLE, STYLISH, CLASSIC, TASTEFUL

Target Market(s)

40 + year olds who are building or rennovating.

Industry/Entity Type

Business

Contact Information for Business Card

Wren
styling, design, homeware

Maren Tulloch
p 0437165093
e maren@wrenliving.com.au
w wrenliving.com.au

Requirements
Must have
• very simple, stylish, classic, sophisticated. Simple and easy to read text that is a print similar to attached image. I like simple round A's though not as in attached image.

Double sided. It wont save as double sided for some reason!!
Should not have
• not too much colour, No animated / cartoon pictures.

```html
<!DOCTYPE html>
<html lang="en">
<head>
<meta charset="utf-8">
<title>Wren — Business Card</title>
<link rel="stylesheet" href="https://fonts.googleapis.com/css2?family=Arimo:wght@400;500&display=swap">
<style>
  :root {
    --backdrop: #d9d9d9;
    --card: #bfdad6;
    --mark-area: #b3cfcb;
    --ink: #1e1e1e;
    --accent: #e2252b;
  }
  * { margin: 0; padding: 0; box-sizing: border-box; }
  html, body {
    width: 1200px;
    height: 960px;
    overflow: hidden;
    background: var(--backdrop);
    font-family: "Arimo", Arial, sans-serif;
    color: var(--ink);
  }
  .canvas { position: relative; width: 1200px; height: 960px; }

  .card {
    position: absolute;
    width: 720px;
    height: 434px;
    background: var(--card);
  }
  .card--contact { left: 78px; top: 22px; }
  .card--brand { left: 344px; top: 456px; }

  /* Contact side */
  .holder {
    position: absolute;
    left: 37px;
    top: 22px;
    font-size: 19px;
    font-variant: small-caps;
    letter-spacing: 0.02em;
    line-height: 1;
  }
  .holder__surname { color: var(--accent); }
  .holder-rule {
    position: absolute;
    left: 37px;
    right: 0;
    top: 51px;
    height: 1px;
    background: var(--accent);
  }
  .contact-list {
    position: absolute;
    left: 40px;
    top: 180px;
    list-style: none;
    font-size: 17px;
    line-height: 24px;
  }
  .contact-list li { display: flex; align-items: center; gap: 8px; }
  .contact-list svg { width: 20px; height: 16px; flex: none; }

  .wordmark {
    position: absolute;
    font-weight: 400;
    color: var(--ink);
    line-height: 1;
  }
  .card--contact .wordmark {
    left: 468px;
    top: 96px;
    font-size: 56px;
    letter-spacing: 0.15em;
  }

  /* Reserved area for the brand mark beneath the wordmark */
  .mark-area {
    position: absolute;
    background: linear-gradient(180deg, var(--card), var(--mark-area) 60%, var(--card));
    border-radius: 4px;
  }
  .card--contact .mark-area { left: 373px; top: 150px; width: 324px; height: 128px; }
  .card--brand .mark-area { left: 136px; top: 128px; width: 444px; height: 180px; }

  /* Brand side */
  .card--brand .wordmark {
    left: 0;
    right: 0;
    top: 54px;
    text-align: center;
    font-size: 68px;
    letter-spacing: 0.16em;
    padding-left: 0.16em;
  }
  .services {
    position: absolute;
    left: 0;
    right: 0;
    top: 352px;
    display: flex;
    justify-content: center;
    align-items: center;
    font-size: 17px;
    list-style: none;
  }
  .services li { position: relative; padding: 0 16px; line-height: 26px; }
  .services li + li::before {
    content: "";
    position: absolute;
    left: 0;
    top: 0;
    width: 2px;
    height: 26px;
    background: var(--accent);
  }
</style>
</head>
<body>
<main class="canvas">

  <section class="card card--contact" aria-label="Business card, contact side">
    <p class="holder">Maren <span class="holder__surname">Tulloch</span></p>
    <div class="holder-rule"></div>

    <ul class="contact-list">
      <li>
        <svg viewBox="0 0 20 16" aria-hidden="true">
          <path fill="var(--accent)" d="M2 6c0-3 4-4 8-4s8 1 8 4l-1 2h-3l-1-2H7L6 8H3z"/>
          <rect x="5" y="8" width="10" height="7" rx="1" fill="var(--accent)"/>
          <circle cx="10" cy="11.5" r="1.8" fill="var(--card)"/>
        </svg>
        <span>0437165093</span>
      </li>
      <li>
        <svg viewBox="0 0 20 16" aria-hidden="true">
          <rect x="2" y="3" width="16" height="11" fill="var(--accent)"/>
          <path d="M2 3l8 6 8-6" fill="none" stroke="var(--card)" stroke-width="1.2"/>
        </svg>
        <span>maren@wrenliving.com.au</span>
      </li>
      <li>
        <svg viewBox="0 0 20 16" aria-hidden="true">
          <g fill="none" stroke="var(--accent)" stroke-width="1.2">
            <circle cx="10" cy="8" r="7"/>
            <ellipse cx="10" cy="8" rx="3" ry="7"/>
            <path d="M3 8h14M4 4.5h12M4 11.5h12"/>
          </g>
        </svg>
        <span>wrenliving.com.au</span>
      </li>
    </ul>

    <p class="wordmark">wren</p>
    <div class="mark-area" role="img" aria-label="Space for the Wren brand mark"></div>
  </section>

  <section class="card card--brand" aria-label="Business card, brand side">
    <p class="wordmark">wren</p>
    <div class="mark-area" role="img" aria-label="Space for the Wren brand mark"></div>
    <ul class="services">
      <li>Decoration</li>
      <li>styling</li>
      <li>Homeware</li>
    </ul>
  </section>

</main>
</body>
</html>
```